Product Label Design for fresh pasta

I manufacture fresh pasta products and am looking for a label design to suit the retail market.

The label size will be 150mm x 105mm.

Industry/Entity Type

Retail

Requirements
Must have
• The label must have the following.
1.Logo
2.Name of Product eg.(Gnocchi)
3.Ingredients list Eg. Potato, Flour (wheat), Parmesan (pastuerized milk, starter cultures, enzymes, rennet, lipase), Egg, Salt, Pepper, Rice flour (coating)
4.Space for a Nutritional information panel
5.cooking instructions Eg. Place gnocchi into boiling salted water, remove once gnocchi start to float (6to7minutes) DO NOT STIR
6. Best before Date
7. Storage instructions Eg. Keep Frozen
8.Needs the phrase (Made in Australia from local and imported ingredients by Il Fornolino, 7/52 Tallowood Crescent, Kelvindale WA 6158)
9. Package size Eg. 500g net
10. Space for a barcode

```html
<!DOCTYPE html>
<html lang="en">
<head>
<meta charset="utf-8">
<title>Il Fornolino Gnocchi Label</title>
<link rel="stylesheet" href="https://fonts.googleapis.com/css2?family=Handlee&family=Marcellus&family=Arimo:wght@400;700&display=swap">
<style>
  :root {
    --backdrop: #bdbdbd;
    --label-white: #ffffff;
    --brand-red: #d9372b;
    --ink: #1e1e1e;
    --soft-ink: #555555;
    --rule: #b9b9b9;
    --barcode-grey: #d6d6d6;
    --photo-green: #e3eed6;
    --photo-red: #f4ddd5;
    --photo-cream: #f5eed6;
  }
  * { box-sizing: border-box; margin: 0; padding: 0; }
  html, body { width: 1200px; height: 1200px; overflow: hidden; background: var(--backdrop); }
  .label {
    position: absolute; left: 233px; top: 87px;
    width: 733px; height: 1026px;
    background: var(--label-white);
    font-family: "Arimo", Arial, sans-serif; color: var(--ink);
    overflow: hidden;
  }
  .brand-tab {
    position: absolute; left: 153px; top: 0; width: 364px; height: 180px;
    background: var(--brand-red);
    border-radius: 0 0 24px 24px;
    display: flex; align-items: center; justify-content: center; gap: 14px;
  }
  .brand-name {
    font-family: "Handlee", cursive; font-size: 50px; color: var(--label-white);
    line-height: 1;
  }
  .brand-dot { width: 20px; height: 20px; background: var(--label-white); }
  .product-name {
    position: absolute; left: 0; right: 0; top: 212px;
    text-align: center; font-family: "Marcellus", serif;
    font-size: 58px; letter-spacing: 4px; color: var(--ink);
  }
  .product-name .accent { color: var(--brand-red); font-size: 48px; letter-spacing: 0; }
  .serving-photo {
    position: absolute; left: 4px; top: 318px; width: 351px; height: 290px;
    border-radius: 24px;
    background: linear-gradient(135deg, var(--photo-green) 0%, var(--photo-red) 45%, var(--photo-cream) 100%);
  }
  .cooking-steps {
    position: absolute; left: 372px; width: 340px; top: 338px;
    text-align: center; font-family: "Handlee", cursive;
    font-size: 25px; line-height: 46px; color: var(--soft-ink);
  }
  .storage { color: var(--brand-red); }
  .net-weight {
    position: absolute; left: 0; width: 733px; top: 636px;
    text-align: center; font-size: 25px; color: var(--brand-red);
  }
  .ingredients {
    position: absolute; left: 22px; top: 702px; width: 216px;
    font-size: 15.5px; line-height: 20px; color: var(--soft-ink);
  }
  .ingredients strong { font-weight: 700; }
  .nutrition {
    position: absolute; left: 247px; top: 700px; width: 473px;
    border: 1px solid var(--rule);
    font-size: 13px; color: var(--soft-ink);
  }
  .nutrition table { width: 100%; border-collapse: collapse; }
  .nutrition td { height: 17px; padding: 0 5px; border-bottom: 1px solid var(--rule); }
  .nutrition td.dv { text-align: center; width: 60px; }
  .nutrition td.split { border-right: 1px solid var(--rule); }
  .nutrition .vitamins { padding: 4px 5px; font-size: 12px; }
  .origin {
    position: absolute; left: 20px; top: 880px; width: 230px;
    text-align: center; font-size: 15px; line-height: 20px; color: var(--soft-ink);
  }
  .best-before {
    position: absolute; left: 332px; top: 902px;
    font-size: 16px; font-weight: 700; color: var(--ink);
  }
  .barcode-space {
    position: absolute; left: 488px; top: 855px; width: 232px; height: 130px;
    background: var(--barcode-grey);
    display: flex; flex-direction: column; align-items: center; justify-content: center;
    font-size: 22px; line-height: 26px; color: var(--ink);
  }
  .footer-band {
    position: absolute; left: 0; bottom: 0; width: 733px; height: 34px;
    background: var(--brand-red); border-radius: 18px 18px 0 0;
  }
</style>
</head>
<body>
<main class="label">
  <header class="brand-tab">
    <span class="brand-name">Il Fornolino</span>
    <span class="brand-dot"></span>
  </header>

  <h1 class="product-name">GNOCCH<span class="accent">i</span></h1>

  <div class="serving-photo" role="img" aria-label="Photo of a fork twirled with pasta, topped with a tomato slice and basil leaves"></div>

  <section class="cooking-steps">
    <p>Place gnocchi into boiling<br>salted water, remove once<br>gnocchi start to float<br>(6 to 7minutes)<br>Do Not Stir</p>
    <p class="storage">Keep Frozen</p>
  </section>

  <p class="net-weight">500g net</p>

  <p class="ingredients"><strong>Ingredients list:</strong> Potato, Flour (wheat), Parmesan (pasteurized milk, starter cultures, enzymes, rennet, lipase), Egg, Salt, Pepper, Rice flour (coating)</p>

  <section class="nutrition">
    <table>
      <tr><td>Amount/Serving</td><td class="dv split">%DV*</td><td>Amount/Serving</td><td class="dv">%DV*</td></tr>
      <tr><td>Fat</td><td class="dv split">#</td><td>Fiber</td><td class="dv">#</td></tr>
      <tr><td>Saturated</td><td class="dv split">#</td><td>Sugar</td><td class="dv">#</td></tr>
      <tr><td>Monounsaturated</td><td class="dv split">#</td><td>Protein</td><td class="dv">#</td></tr>
      <tr><td>Omega 3</td><td class="dv split">#</td><td>Phytic Acid</td><td class="dv">#</td></tr>
      <tr><td>Omega 6</td><td class="dv split">#</td><td>ORAC</td><td class="dv">#</td></tr>
    </table>
    <p class="vitamins">Vit A # , Vit C # , Vit E # , Calcium # , Iron #</p>
  </section>

  <p class="origin">Made in Australia from local and imported ingredients by Il Fornolino, 7/52 Tallowood Crescent, Kelvindale WA 6158</p>

  <p class="best-before">Best before:</p>

  <div class="barcode-space"><span>bar code</span><span>29,83 x 21mm</span></div>

  <div class="footer-band"></div>
</main>
</body>
</html>
```